I am about to have my Grandma's memoir printed. I am planning to go with an image wrap soft cover. The book is B5 page size 6.9" X 9.8" I am looking for help to make the cover for this special project stand out in a good way. I have included some photos that could be used but it's not necessary to use all of them, they are only provided to give an idea about the tone of the book being a picture of her whole life from being raised on a homestead, to living all the way through the modern era.

Requirements
Must have
• A feel that supports the title of the book "Willowmere Lanterns"

```html
<!DOCTYPE html>
<html lang="en">
<head>
<meta charset="utf-8">
<title>Willowmere Lanterns – Cover Wrap</title>
<link href="https://fonts.googleapis.com/css2?family=Cinzel:wght@500;700&family=Rye&display=swap" rel="stylesheet">
<style>
  :root {
    --page-bg: #e9e7e3;
    --cloth-dark: #6e4c40;
    --cloth-mid: #8d6a5f;
    --cloth-light: #c7b5b1;
    --cream-type: #f3efe6;
    --title-gold: #e9e39c;
    --title-edge: #5a4a1c;
    --maroon: #4a1414;
    --photo-border: #f7f5f0;
  }
  html, body {
    margin: 0;
    width: 1200px;
    height: 1200px;
    overflow: hidden;
    background: var(--page-bg);
  }
  .cover-wrap {
    position: absolute;
    left: 50px;
    top: 225px;
    width: 1100px;
    height: 750px;
    overflow: hidden;
    background:
      radial-gradient(ellipse 520px 380px at 930px 620px, var(--cloth-light) 0%, rgba(199,181,177,0) 100%),
      linear-gradient(125deg, var(--cloth-dark) 0%, var(--cloth-mid) 40%, #9c7c72 62%, var(--cloth-light) 100%);
    box-shadow: 0 8px 18px rgba(0,0,0,.45);
  }
  .light-band {
    position: absolute;
    inset: 0;
    background: linear-gradient(120deg, rgba(0,0,0,0) 30%, rgba(255,255,255,.10) 42%, rgba(0,0,0,0) 55%);
  }
  .back-title {
    position: absolute;
    left: 40px;
    width: 450px;
    top: 58px;
    text-align: center;
    font-family: "Cinzel", serif;
    font-weight: 500;
    color: var(--cream-type);
    text-shadow: 1px 1px 2px rgba(0,0,0,.5);
  }
  .back-title .name { font-size: 27px; letter-spacing: .5px; }
  .back-title .sub { font-size: 20px; margin-top: 2px; }
  .snapshot {
    position: absolute;
    border: 8px solid var(--photo-border);
    box-shadow: 3px 5px 10px rgba(0,0,0,.45);
  }
  .snapshot--living-room {
    left: 82px; top: 188px; width: 285px; height: 185px;
    transform: rotate(-11deg);
    background: linear-gradient(160deg, #d9d9d6, #8d8d8a 55%, #4e4e4c);
  }
  .snapshot--couple {
    left: 145px; top: 378px; width: 280px; height: 210px;
    transform: rotate(3deg);
    background: linear-gradient(140deg, #b49a92, #8b6f66 45%, #3f6f7a 70%, #c9a96a);
  }
  .spine-text {
    position: absolute;
    left: 528px;
    top: 30px;
    width: 40px;
    height: 690px;
    writing-mode: vertical-rl;
    font-family: "Cinzel", serif;
    font-weight: 500;
    font-size: 19px;
    color: var(--cream-type);
    text-shadow: 1px 1px 2px rgba(0,0,0,.5);
    white-space: nowrap;
  }
  .spine-text span { margin-bottom: 22px; }
  .spine-text .small { font-size: 15px; }
  .front-title {
    position: absolute;
    left: 580px;
    width: 500px;
    top: 32px;
    text-align: center;
    font-family: "Rye", serif;
    color: var(--title-gold);
    text-shadow: -1px -1px 0 var(--title-edge), 2px 2px 0 var(--title-edge), 3px 4px 6px rgba(0,0,0,.45);
    line-height: 1.05;
  }
  .front-title .line-one { font-size: 64px; display: block; }
  .front-title .line-two { font-size: 72px; display: block; }
  .front-subtitle {
    position: absolute;
    left: 580px;
    width: 500px;
    top: 242px;
    text-align: center;
    font-family: "Cinzel", serif;
    font-weight: 700;
    font-size: 25px;
    color: var(--maroon);
  }
  .rider-vignette {
    position: absolute;
    left: 590px;
    top: 292px;
    width: 510px;
    height: 400px;
    background:
      radial-gradient(ellipse 230px 110px at 280px 270px, rgba(240,240,240,.95), rgba(240,240,240,0) 100%),
      radial-gradient(ellipse 260px 200px at 260px 190px, #5e7a4c 0%, #8fa279 55%, rgba(143,162,121,0) 100%);
  }
  .author {
    position: absolute;
    left: 580px;
    width: 500px;
    top: 688px;
    text-align: center;
    font-family: "Cinzel", serif;
    font-weight: 700;
    font-size: 26px;
    color: var(--maroon);
  }
</style>
</head>
<body>
  <section class="cover-wrap">
    <div class="light-band"></div>

    <div class="back-title">
      <div class="name">Willowmere Lanterns</div>
      <div class="sub">A Memoir</div>
    </div>
    <div class="snapshot snapshot--living-room" role="img" aria-label="Black-and-white snapshot of a woman seated on a sofa in a living room"></div>
    <div class="snapshot snapshot--couple" role="img" aria-label="Colour snapshot of an older couple standing together indoors"></div>

    <div class="spine-text">
      <span>Willowmere Lanterns</span>
      <span class="small">A Memoir</span>
      <span class="small">Marian Ashby Holloway</span>
    </div>

    <h1 class="front-title">
      <span class="line-one">Willowmere</span>
      <span class="line-two">Lanterns</span>
    </h1>
    <div class="front-subtitle">A Memoir</div>
    <div class="rider-vignette" role="img" aria-label="Vintage tinted photograph of a young woman in a hat riding a pale horse beside an old car, trees behind"></div>
    <div class="author">Marian Ashby Holloway</div>
  </section>
</body>
</html>
```